Professional violinist needs business cards

I am trying to attract the following jobs:
-private violin lessons (primarily classical)
-performance gigs (weddings, birthday parties, funerals, etc.)
-collaborations with other artists (studio recordings, performances)

I want to communicate that I have a very high standard of excellence for my work, but I also love people and celebrations.
Values/style words I like are:
love, joy, peace, fun, beauty, authenticity, excellence, warmth, refined/sleek, free spirited. If that's too confusing, just ignore :)

I will attach my favorite business card template that I could find on Canva. The lines are supposed to be like a music staff, which I think is really cool, but I also don't want it to look too busy. I like the simple black and white--I think it looks sharp--but I also am open to other ideas. I also have seen business cards with pictures included that looked great, so I attached an image that could be used as well.

I am also attaching a file that I made of my initials that could be used as a logo, but I'm not sure if it should be included.

Information on the card:
-My name (18 letters total)
-"violinist"
-phone number, email, website

Thank you!

```html
<!DOCTYPE html>
<html lang="en">
<head>
<meta charset="utf-8">
<title>Helena Marlowe – Violinist Business Cards</title>
<link href="https://fonts.googleapis.com/css2?family=Dancing+Script:wght@500&family=Cinzel:wght@500&family=Libre+Baskerville&display=swap" rel="stylesheet">
<style>
  :root {
    --backdrop: #2b2b2c;
    --card-dark: #23272c;
    --card-wall: #2a2b2c;
    --ink-light: #ece6dc;
    --gold: #cbb898;
    --rule: #a8977a;
    --photo-warm-1: #6b5a45;
    --photo-warm-2: #2a221c;
    --photo-dress: #141414;
  }
  * { margin: 0; padding: 0; box-sizing: border-box; }
  html, body {
    width: 1200px; height: 1138px; overflow: hidden;
    background: var(--backdrop);
  }
  .canvas { position: relative; width: 1200px; height: 1138px; }

  .card {
    position: absolute;
    left: 276px;
    width: 620px; height: 376px;
    border-radius: 14px;
    overflow: hidden;
  }
  .card--front { top: 186px; background: var(--card-dark); }
  .card--back {
    top: 608px;
    background: linear-gradient(135deg, #303132 0%, var(--card-wall) 55%, #1f2021 100%);
  }

  .card__photo {
    position: absolute; left: 0; top: 0;
    width: 224px; height: 100%;
  }
  .card--front .card__photo {
    background: linear-gradient(180deg, var(--photo-warm-1) 0%, #4a3d31 45%, var(--photo-warm-2) 100%);
  }
  .card--back .card__photo {
    background: linear-gradient(90deg, var(--photo-dress) 0%, #1d1a18 55%, #3a2a1e 100%);
  }

  .card__identity {
    position: absolute;
    left: 280px; width: 292px;
    text-align: center;
  }
  .card--front .card__identity { top: 98px; }
  .card--back .card__identity { top: 62px; }

  .logo-mark {
    display: inline-flex; align-items: center; gap: 7px;
    font-family: "Dancing Script", cursive;
    font-weight: 500;
    font-size: 20px;
    color: var(--gold);
    height: 52px;
  }
  .logo-mark__dot {
    width: 8px; height: 8px; border-radius: 50%;
    background: var(--gold);
  }

  .card__name {
    font-family: "Dancing Script", cursive;
    font-weight: 500;
    font-size: 30px;
    color: var(--ink-light);
    letter-spacing: 0.3px;
    margin-top: 2px;
    white-space: nowrap;
  }

  .card__title {
    display: flex; align-items: center; justify-content: center;
    gap: 14px;
    margin-top: 2px;
    font-family: "Cinzel", serif;
    font-weight: 500;
    font-size: 15px;
    letter-spacing: 2.5px;
    color: var(--ink-light);
  }
  .card__title::before,
  .card__title::after {
    content: ""; display: block;
    width: 72px; height: 1px;
    background: var(--rule);
  }

  .card__contact {
    margin-top: 20px;
    font-family: "Libre Baskerville", serif;
    font-size: 13.5px;
    line-height: 23px;
    color: var(--ink-light);
    list-style: none;
  }
  .card__contact .accent { color: var(--gold); }
</style>
</head>
<body>
<main class="canvas">

  <section class="card card--front" aria-label="Business card front">
    <div class="card__photo" role="img" aria-label="Photo of the violinist in a black dress holding her violin and bow beside a stone wall staircase"></div>
    <div class="card__identity">
      <div class="logo-mark"><span class="logo-mark__dot"></span>H. Marlowe</div>
      <h1 class="card__name">Helena Marlowe</h1>
      <p class="card__title">VIOLINIST</p>
    </div>
  </section>

  <section class="card card--back" aria-label="Business card back">
    <div class="card__photo" role="img" aria-label="Close-up photo of a hand holding a violin and bow against a black dress"></div>
    <div class="card__identity">
      <div class="logo-mark"><span class="logo-mark__dot"></span>H. Marlowe</div>
      <h2 class="card__name">Helena Marlowe</h2>
      <p class="card__title">VIOLINIST</p>
      <ul class="card__contact">
        <li>+1 (555) 014-2287</li>
        <li>Helena@HelenaMarlowe.com</li>
        <li>www.<span class="accent">HelenaMarlowe</span>.com</li>
        <li>Richmond, VA</li>
      </ul>
    </div>
  </section>

</main>
</body>
</html>
```